Catalogue for Mobile charging stations with image and specifications about each model

I need a simple and clean catalogue that shows our products clearly with the specifications about them. something simple for potential clients to browse through and choose what fits their venue best.

I have attached 1 example of product page and 1 of the last page. This is just a reference on how simple and clean i want it, but you can design it however you want if you have a better idea. I want something professional

also i will attach our current logo (we will change it shortly but colors will remain the same so you can have an idea of color theme)
Updates

Project Deadline Extended Reason: Hello, i am extending this project by 5 days as I think only 5 days is too little Good luck everyone I'm looking forward to seeing all great designs!BestLiliana Added Tuesday, October 3, 2017

Target Market(s)

All types of companies

Font styles to use
Script

Colors

Designer to choose colors to be used in the design.

Requirements
Must have
• The catalogue will include about 60 products and specifications. I will provide you with images for all products and the specifications.
Nice to have
• A nice design that catches the viewers attention, not too complicated but simple and professional
• Our logo is green and black. so maybe best to stick with this color theme
• There are about 10 products missing from the files I sent with all the images and specification. These will be the last ones to be added as I am still waiting for some information
Should not have
• Too much design and patterns that makes it hard to focus on the product and information

```html
<!DOCTYPE html>
<html lang="en">
<head>
<meta charset="utf-8">
<title>VoltNest Product Catalog 2017–2018</title>
<link href="https://fonts.googleapis.com/css2?family=Raleway:wght@200;300;400;600&family=Open+Sans:wght@400;600&display=swap" rel="stylesheet">
<style>
  :root{
    --backdrop:#6a6a6a;
    --paper:#f1f1f1;
    --tile-light:#dcdcdc;
    --tile-dark:#4b4b50;
    --green:#5cb85f;
    --green-soft:#7cc47e;
    --ink:#4a4a4a;
    --ink-soft:#777;
    --rule-dark:#555559;
  }
  *{box-sizing:border-box;margin:0;padding:0}
  html,body{width:1200px;height:800px;overflow:hidden}
  body{background:var(--backdrop);font-family:"Raleway",sans-serif;position:relative}
  .spread{position:absolute;left:105px;top:50px;width:990px;height:700px;display:flex;box-shadow:0 18px 40px rgba(0,0,0,.35)}
  .page{position:relative;width:495px;height:700px;background:var(--paper);overflow:hidden}
  .page--back{border-right:1px solid #d4d4d4}
  .tile{position:absolute;width:80px;height:80px}
  .tile--light{background:var(--tile-light)}
  .tile--dark{background:var(--tile-dark)}
  .tile--green{background:var(--green)}
  .photo{position:absolute}
  .photo--team{left:190px;top:80px;width:160px;height:160px;background:linear-gradient(135deg,#8a7a6a,#3e4248 60%,#6b7f95)}
  .map{position:absolute;left:270px;top:240px;width:225px;height:460px;
       background:linear-gradient(90deg,rgba(241,241,241,1) 0%,rgba(241,241,241,0) 25%),linear-gradient(160deg,#e6e2d6,#cfdcc4 45%,#dfe2dc 80%)}
  .support{position:absolute;left:40px;top:268px;width:235px}
  .support h3{font-weight:600;font-size:10px;color:var(--green);margin-bottom:8px}
  .support p{font-size:6.5px;line-height:1.5;color:var(--ink-soft);margin-bottom:6px}
  .brand{display:flex;align-items:center;gap:6px}
  .brand__dot{width:12px;height:12px;border-radius:50%;background:var(--green)}
  .brand__name{font-weight:600;color:var(--green)}
  .brand__sub{font-size:6px;letter-spacing:2px;color:var(--ink-soft);text-transform:lowercase}
  .back-brand{position:absolute;left:70px;top:420px}
  .back-brand .brand__name{font-size:15px}
  .back-brand .brand__sub{margin-left:18px;margin-top:2px}
  .contacts{position:absolute;left:40px;top:480px;list-style:none}
  .contacts li{display:flex;align-items:center;gap:8px;font-size:6px;color:var(--ink-soft);margin-bottom:10px;font-family:"Open Sans",sans-serif}
  .contacts svg{width:11px;height:11px;fill:var(--ink)}
  .front-brand{position:absolute;left:0;right:0;top:78px;display:flex;flex-direction:column;align-items:center}
  .front-brand .brand__name{font-size:22px}
  .front-brand .brand__sub{margin-top:3px;margin-left:16px}
  .tagline{position:absolute;left:0;right:0;top:146px;text-align:center;font-weight:200;font-size:15px;letter-spacing:3px;color:#9a9a9a}
  .rule{position:absolute;left:0;width:495px}
  .rule--green{top:200px;height:5px;background:var(--green)}
  .rule--dark{top:582px;height:5px;background:var(--rule-dark)}
  .product-grid{position:absolute;left:22px;top:214px;display:grid;grid-template-columns:repeat(5,86px);grid-template-rows:repeat(4,86px);gap:4px}
  .cell--light{background:var(--tile-light)}
  .cell--dark{background:var(--tile-dark)}
  .cell--green{background:var(--green)}
  .cell--station{background:linear-gradient(160deg,#e8eee6,#6fa86c)}
  .cell--phone{background:linear-gradient(135deg,#c9b3a6,#7b6f6a)}
  .cell--powerbank{background:linear-gradient(135deg,#f4f4f4,#8fcf7b)}
  .cell--friends{background:linear-gradient(135deg,#d35a4a,#4f6d96)}
  .cell--kiosk{background:linear-gradient(160deg,#eaeaea,#596270)}
  .cell--team{background:linear-gradient(135deg,#8a7a6a,#3e4248 60%,#6b7f95)}
  .cell--stand{background:linear-gradient(160deg,#e4e4e4,#b8b8b8)}
  .cell--counter{background:linear-gradient(160deg,#d9dde2,#b9332a 70%,#e8b83a)}
  .catalog-title{position:absolute;left:40px;top:608px;font-size:24px;font-weight:200;color:var(--green);letter-spacing:.5px}
  .catalog-title span{color:var(--ink)}
  .web{position:absolute;left:40px;top:652px;font-family:"Open Sans",sans-serif;font-weight:600;font-size:11px;color:var(--ink)}
</style>
</head>
<body>
<main class="spread">
  <section class="page page--back">
    <div class="tile tile--light" style="left:190px;top:0"></div>
    <div class="tile tile--green" style="left:270px;top:0"></div>
    <div class="tile tile--dark" style="left:350px;top:0"></div>
    <div class="tile tile--light" style="left:430px;top:0"></div>
    <div class="tile tile--dark" style="left:110px;top:80px"></div>
    <div class="photo photo--team" role="img" aria-label="Photo of friends sharing their phones"></div>
    <div class="tile tile--light" style="left:350px;top:80px"></div>
    <div class="tile tile--dark" style="left:430px;top:80px"></div>
    <div class="tile tile--green" style="left:350px;top:160px"></div>
    <div class="map" role="img" aria-label="Street map of Harbourview with office location pin"></div>

    <div class="support">
      <h3>Customer Support</h3>
      <p>If you can not find any answer to your question in our knowledgeable FAQs and need further assistance, please email hello@voltnest-power.com or use the live chat option for quicker assistance.</p>
      <p>Our Customer Support office hours are M-F 9a-5p CEST (excluding major holidays). We will answer your ticket in the order in which they have been received. Please allow up to 48 hours for a customer support agent to respond.</p>
    </div>

    <div class="back-brand">
      <div class="brand"><span class="brand__dot"></span><span class="brand__name">VoltNest</span></div>
      <div class="brand__sub">charging solutions</div>
    </div>

    <ul class="contacts">
      <li><svg viewBox="0 0 12 12"><path d="M6 0a4 4 0 0 0-4 4c0 3 4 8 4 8s4-5 4-8a4 4 0 0 0-4-4zm0 5.5A1.5 1.5 0 1 1 6 2.5a1.5 1.5 0 0 1 0 3z"/></svg>Marisol, 12 Harbour Lane, Suite 4, Harbourview 41101</li>
      <li><svg viewBox="0 0 12 12"><path d="M3 1l2 2-1 2c1 1.5 2 2.5 3 3l2-1 2 2-2 2C4 11 1 8 1 3z"/></svg>555 014 2760</li>
      <li><svg viewBox="0 0 12 12"><path d="M1 2h10v8H1zm1 1v.5l4 3 4-3V3z"/></svg>hello@voltnest-power.com</li>
      <li><svg viewBox="0 0 12 12"><circle cx="6" cy="6" r="5" fill="none" stroke="#4a4a4a" stroke-width="1.2"/><path d="M1 6h10M6 1c2 2 2 8 0 10M6 1c-2 2-2 8 0 10" fill="none" stroke="#4a4a4a" stroke-width=".8"/></svg>www.voltnest-power.com</li>
    </ul>
  </section>

  <section class="page page--front">
    <div class="front-brand">
      <div class="brand"><span class="brand__dot"></span><span class="brand__name">VoltNest</span></div>
      <div class="brand__sub">charging solutions</div>
    </div>
    <p class="tagline">Fast charge technology...</p>
    <div class="rule rule--green"></div>

    <div class="product-grid">
      <div class="cell--station" role="img" aria-label="Wall charging station product"></div>
      <div class="cell--green"></div>
      <div class="cell--light"></div>
      <div class="cell--light"></div>
      <div class="cell--light"></div>

      <div class="cell--dark"></div>
      <div class="cell--phone" role="img" aria-label="Hand holding a smartphone"></div>
      <div class="cell--powerbank" role="img" aria-label="Green power bank charging a phone"></div>
      <div class="cell--dark"></div>
      <div class="cell--friends" role="img" aria-label="Friends looking at their phones"></div>

      <div class="cell--kiosk" role="img" aria-label="Floor kiosk charging station"></div>
      <div class="cell--dark"></div>
      <div class="cell--team" role="img" aria-label="Group of friends sharing phones"></div>
      <div class="cell--stand" role="img" aria-label="Standing locker charging tower"></div>
      <div class="cell--green"></div>

      <div class="cell--light"></div>
      <div class="cell--light"></div>
      <div class="cell--dark"></div>
      <div class="cell--light"></div>
      <div class="cell--counter" role="img" aria-label="Countertop charging station in a restaurant"></div>
    </div>
    <div class="rule rule--dark"></div>

    <h1 class="catalog-title">Product Catalog <span>2017-2018</span></h1>
    <p class="web">www.voltnest-power.com</p>
  </section>
</main>
</body>
</html>
```